Industrial Professional Business Card Design (Vantrel Systems)

Would like professional looking business cards. Not too busy leaning towards minimal. Should have a slogan like:
"Industrial Automation and Control".

We are a tech company that programs industrial PLC computers. We also develop custom hardware solutions. Please use the logo for inspiration.

Target Market(s)

Mining, industrial, processing, automation, factory

Industry/Entity Type

Engineering

Contact Information for Business Card

Name, phone, email, website. job title.

Font styles to use
Other font styles liked:
• droid sans

Requirements
Must have
• Use colours that go well with the logo. Not too busy design.

```html
<!DOCTYPE html>
<html lang="en">
<head>
<meta charset="utf-8">
<title>Vantrel Systems – Business Card</title>
<link rel="stylesheet" href="https://fonts.googleapis.com/css2?family=Noto+Sans:wght@400;700&display=swap">
<style>
  :root {
    --bg-deep: #050505;
    --bg-panel: #0d0e10;
    --bg-slant: #15171a;
    --orange: #f26a21;
    --brand-blue: #2c6c9c;
    --band-top: #1c4a78;
    --band-bottom: #12365c;
    --rule: #1b1f26;
    --glow: #35c8ff;
    --white: #ffffff;
  }
  * { margin: 0; padding: 0; box-sizing: border-box; }
  html, body {
    width: 1200px; height: 686px; overflow: hidden;
    background: var(--bg-deep);
    font-family: "Noto Sans", "Droid Sans", sans-serif;
  }
  .card {
    position: relative; width: 1200px; height: 686px; overflow: hidden;
    background: var(--bg-deep);
  }
  .card__panel {
    position: absolute; left: 0; top: 44px; width: 1200px; height: 430px;
    background: linear-gradient(180deg, var(--bg-panel), #080809);
  }
  .card__slant {
    position: absolute; inset: 0;
  }
  .brand {
    position: absolute; left: 74px; top: 70px; width: 552px; height: 380px;
  }
  .brand__mark {
    position: absolute; left: 156px; top: 8px;
    width: 240px; height: 240px; border-radius: 50%;
    background: var(--brand-blue);
  }
  .brand__name {
    position: absolute; left: 0; top: 268px; width: 552px;
    text-align: center; font-size: 62px; font-weight: 400;
    color: var(--brand-blue); line-height: 1; white-space: nowrap;
  }
  .person {
    position: absolute; left: 740px; top: 104px; width: 400px; text-align: center;
  }
  .person__business {
    font-size: 43px; font-weight: 700; color: var(--orange); line-height: 1.1;
  }
  .person__title {
    margin-top: 6px; font-size: 34px; font-weight: 400; color: var(--white); line-height: 1.2;
  }
  .contacts {
    position: absolute; left: 766px; top: 276px; list-style: none;
  }
  .contacts__item {
    display: flex; align-items: center; height: 50px;
    font-size: 27px; color: var(--white); letter-spacing: 0.3px;
  }
  .contacts__icon {
    width: 26px; height: 26px; margin-right: 16px; flex: none;
  }
  .rule {
    position: absolute; left: 0; width: 1200px; height: 8px;
    background: var(--rule);
  }
  .rule::after {
    content: ""; position: absolute; left: 380px; right: 380px; top: 3px; height: 2px;
    background: linear-gradient(90deg, transparent, var(--glow), transparent);
    box-shadow: 0 0 8px var(--glow);
  }
  .rule--upper { top: 497px; }
  .rule--lower { top: 626px; }
  .slogan {
    position: absolute; left: 0; top: 523px; width: 1200px; height: 89px;
    background: linear-gradient(180deg, var(--band-top), var(--band-bottom));
    display: flex; align-items: center; justify-content: center;
    font-size: 49px; font-weight: 700; color: var(--white); letter-spacing: 0.5px;
  }
</style>
</head>
<body>
<main class="card">
  <div class="card__panel"></div>
  <svg class="card__slant" width="1200" height="686" viewBox="0 0 1200 686" aria-hidden="true">
    <polygon points="588,0 1200,0 1200,474 754,474" fill="var(--bg-slant)" opacity="0.55"/>
  </svg>

  <section class="brand">
    <div class="brand__mark"></div>
    <p class="brand__name">Vantrel Systems</p>
  </section>

  <section class="person">
    <h1 class="person__business">Business Name</h1>
    <p class="person__title">Job Title</p>
  </section>

  <ul class="contacts">
    <li class="contacts__item">
      <svg class="contacts__icon" viewBox="0 0 24 24" aria-hidden="true">
        <path fill="#fff" d="M6.6 10.8a15.1 15.1 0 0 0 6.6 6.6l2.2-2.2a1 1 0 0 1 1-.25 11.4 11.4 0 0 0 3.6.57 1 1 0 0 1 1 1V20a1 1 0 0 1-1 1A17 17 0 0 1 3 4a1 1 0 0 1 1-1h3.5a1 1 0 0 1 1 1c0 1.25.2 2.45.57 3.6a1 1 0 0 1-.25 1z"/>
        <path fill="none" stroke="#fff" stroke-width="1.6" stroke-linecap="round" d="M14 3.5a7 7 0 0 1 6.5 6.5M14 7a3.5 3.5 0 0 1 3 3"/>
      </svg>
      <span>+00 1234 5678 9012</span>
    </li>
    <li class="contacts__item">
      <svg class="contacts__icon" viewBox="0 0 24 24" aria-hidden="true">
        <rect x="2" y="6" width="20" height="13" fill="#fff"/>
        <path d="M2.5 6.5 12 13.5l9.5-7" fill="none" stroke="#000" stroke-width="1.4"/>
      </svg>
      <span>info@vantrelmail.com</span>
    </li>
    <li class="contacts__item">
      <svg class="contacts__icon" viewBox="0 0 24 24" aria-hidden="true">
        <g fill="none" stroke="#fff" stroke-width="1.5">
          <circle cx="12" cy="12" r="9"/>
          <ellipse cx="12" cy="12" rx="4" ry="9"/>
          <path d="M3 12h18M4.5 7.5h15M4.5 16.5h15"/>
        </g>
      </svg>
      <span>www.vantrelsystems.com</span>
    </li>
  </ul>

  <div class="rule rule--upper"></div>
  <p class="slogan">Industrial Automation and Control</p>
  <div class="rule rule--lower"></div>
</main>
</body>
</html>
```